Frandivo tri-fold brochure, letterhead, business cards, envelopes.

I need a professional looking flyer that will appeal to shipping managers, dispatchers, etc. who don't have a lot of time. I'm Golden Lane Arbiter (title is a registered trademark) arranging freight transportation at the lowest possible cost to the shipper. I contract with shippers and then find truckers in the area that will backhaul and thus give the shipper a discounted transportation rate. I let the shipper tell me the rate they want to pay and I negotiate with trucking companies to find that rate. I'll upload the topics I want to convey. Keep in mind that the brochure has to be eye catching enough on the first page to entice them to read on. I want to tie into my website design a bit if possible. It's a simple site so I don't know just how well that'll work. I do want the brochure, business cards, letterhead and envelopes to tie in with each other. I'd like my picture on the brochure somewhere.

Target Market(s)

Shipping managers, trucking dispatchers.

Industry/Entity Type

Truckline Operation

Contact Information for Business Card

Professional design that will set off the logo colors.

Font styles to use
Serif
Sans Serif

Colors

Designer to choose colors to be used in the design.

Requirements
Must have
• Milo Tarvinske, GOLDEN LANE ARBITERīƒ’
• Phone: 855-417-6093
• Email: Milo@frandivo.example
• Website: www.frandivo.example
• Business logo with "TM" to indicate trademark registration has been files.
• Tag line "Fast Shipping Relief".
• My photo.
Nice to have
• Address: 3157 N. Wexford Avenue, #51806
• Denver, CO 80219

```html
<!DOCTYPE html>
<html lang="en">
<head>
<meta charset="utf-8">
<title>Frandivo Freight – Trifold Outside</title>
<link rel="stylesheet" href="https://fonts.googleapis.com/css2?family=Open+Sans:ital,wght@0,400;0,600;0,700;1,400&family=PT+Sans+Narrow:wght@400;700&family=Orbitron:wght@700;900&display=swap">
<style>
  :root{
    --red:#d4202a;
    --red-dark:#b3141c;
    --grey:#a9a9a9;
    --grey-light:#c4c4c4;
    --grey-dark:#8d8d8d;
    --text:#555;
    --white:#fff;
    --stage:#5d7476;
  }
  *{box-sizing:border-box;margin:0;padding:0}
  html,body{width:1200px;height:1200px;overflow:hidden;background:var(--stage)}
  .brochure{position:absolute;left:90px;top:240px;width:1020px;height:720px;display:flex;box-shadow:0 20px 40px rgba(0,0,0,.25)}
  .panel{position:relative;width:340px;height:720px;overflow:hidden}

  /* Inner flap */
  .panel--flap{background:var(--white);font-family:"PT Sans Narrow",sans-serif;color:var(--text)}
  .flap-head{position:absolute;left:24px;top:28px;right:20px}
  .flap-head h2{font-weight:400;font-size:22px;line-height:1.15;color:#777}
  .flap-head h2 strong{color:var(--red);font-weight:700;text-transform:uppercase}
  .flap-head h2 .big{font-size:27px}
  .flap-head p{margin-top:14px;font-size:16px;line-height:1.2;color:#777}
  .bullets{list-style:none}
  .bullets li{position:relative;padding-left:14px;font-size:12.5px;line-height:1.25;margin-bottom:16px;color:#666}
  .bullets li::before{content:"»";position:absolute;left:0;top:-2px;color:var(--red);font-weight:700;font-size:15px}
  .flap-bullets{position:absolute;left:24px;right:20px;top:182px}
  .flap-photo{position:absolute;left:0;right:0;top:402px;height:150px;background:linear-gradient(120deg,#f4f4f4 0%,#f4f4f4 35%,#c8222b 55%,#8e1117 75%,#e9e9e9 100%)}
  .flap-band{position:absolute;left:0;right:0;top:560px;height:98px;background:linear-gradient(#bdbdbd,#a8a8a8);padding:20px 20px 0 24px}
  .flap-band .bullets li{color:#fff;margin-bottom:12px}
  .flap-foot{position:absolute;left:0;right:0;bottom:0;height:62px;display:flex;align-items:center;justify-content:center;font-family:"Open Sans",sans-serif;font-size:12px;letter-spacing:5px;color:#666}

  /* Back panel */
  .panel--contact{background:linear-gradient(#bcbcbc,#a2a2a2 60%,#b0b0b0);border-left:14px solid var(--red);border-right:14px solid var(--red);font-family:"Open Sans",sans-serif}
  .network{position:absolute;left:0;right:0;top:96px;text-align:center}
  .network h2{color:var(--red);font-weight:700;font-size:20px;line-height:1.4}
  .network p{margin-top:26px;color:#555;font-weight:600;font-size:13px;line-height:1.35}
  .network p strong{color:var(--red);font-size:15px;font-weight:700}
  .contact-band{position:absolute;left:0;right:0;top:332px;height:36px;background:var(--red)}
  .contact-photo{position:absolute;left:18px;top:318px;width:132px;height:140px;border:3px solid var(--red);background:radial-gradient(circle at 50% 40%,#7fe3ef,#1aa8c4 70%,#0d7f98)}
  .contact-name{position:absolute;left:162px;top:337px;color:var(--white)}
  .contact-name h3{font-size:12px;font-weight:700}
  .contact-name em{font-size:11px;display:block;margin-top:1px}
  .contact-list{position:absolute;left:162px;top:380px;list-style:none;color:var(--white);font-size:10.5px}
  .contact-list li{display:flex;align-items:flex-start;gap:5px;margin-bottom:8px;line-height:1.8;margin-top:-4px}
  .contact-list li span{display:block}
  .contact-list svg{width:9px;height:9px;margin-top:5px;flex:none;fill:var(--white)}
  .contact-list .strong{font-weight:700}
  .box-truck{position:absolute;left:14px;right:14px;top:574px;height:128px;background:linear-gradient(90deg,#e6e6e6,#fafafa 40%,#f0f0f0);border-radius:3px;display:flex;align-items:center;justify-content:flex-end;padding-right:22px}
  .box-truck .brand{font-family:"Open Sans",sans-serif;font-weight:700;font-size:13px;color:var(--red)}

  /* Front cover */
  .panel--cover{background:var(--grey);border-left:14px solid var(--red)}
  .cover-photo{position:absolute;left:0;right:0;top:0;height:578px;background:linear-gradient(180deg,#d7f1ee 0%,#eef6f3 28%,#8bb9c6 48%,#2f7f9c 62%,#6b6b6b 80%,#3e3e3e 100%)}
  .cover-brand{position:absolute;left:0;right:0;top:70px;text-align:center;font-family:"Open Sans",sans-serif;font-weight:700;font-size:22px;color:var(--red)}
  .cover-band{position:absolute;left:0;right:0;top:578px;height:90px;background:linear-gradient(#b1b1b1,#9a9a9a);text-align:center;font-family:"Orbitron",sans-serif}
  .cover-band .fast{display:block;padding-top:4px;color:var(--red);font-weight:900;font-size:32px;letter-spacing:1px}
  .cover-band .relief{display:block;margin-top:2px;color:var(--white);font-weight:700;font-size:22px;letter-spacing:1px}
  .cover-foot{position:absolute;left:0;right:16px;bottom:0;height:52px;background:var(--white);text-align:center;font-family:"Open Sans",sans-serif;color:#444}
  .cover-foot .phone{display:flex;align-items:center;justify-content:center;gap:6px;padding-top:8px;font-weight:700;font-size:16px;letter-spacing:1px}
  .cover-foot .phone svg{width:12px;height:12px;fill:#444}
  .cover-foot .web{display:block;font-size:10px;letter-spacing:4px;margin-top:2px}
  .cover-corner{position:absolute;right:0;bottom:0;width:16px;height:60px;background:var(--red)}
</style>
</head>
<body>
<main class="brochure">

  <section class="panel panel--flap">
    <header class="flap-head">
      <h2>We find reliable trucks <strong>quickly</strong><br><span class="big">and at the <strong>best rate</strong></span></h2>
      <p>You tell us the rate you want to pay and we'll negotiate that rate for you.</p>
    </header>
    <ul class="bullets flap-bullets">
      <li>We are GOLDEN LANE ARBITERS® trained to the highest standard of proficiency.</li>
      <li>Top quality management who understand your business processes, goals and requirements.</li>
      <li>In the event of a loss or damage claim we negotiate that claim on your behalf AT NO COST TO YOU.</li>
      <li>We distinguish ourselves with the expertise to fulfill ALL our customers' information technological needs.</li>
    </ul>
    <div class="flap-photo" role="img" aria-label="Photo of a red semi truck cab pulling a white trailer"></div>
    <div class="flap-band">
      <ul class="bullets">
        <li>Ability to add value to multiple parts of your organization.</li>
        <li>Our team of professionals is continually updated on evolving industry trends.</li>
      </ul>
    </div>
    <footer class="flap-foot">WWW.FRANDIVO.EXAMPLE</footer>
  </section>

  <section class="panel panel--contact">
    <div class="network">
      <h2>WITH A NETWORK OF<br>over 7,000 Motor Carriers</h2>
      <p>we are able to locate backhaulers<br>that match your shipping and<br><strong>TRANSPORTATION NEEDS.</strong></p>
    </div>
    <div class="contact-band"></div>
    <div class="contact-photo" role="img" aria-label="Portrait photo of Milo Tarvinske"></div>
    <div class="contact-name">
      <h3>Milo Tarvinske</h3>
      <em>Golden Lane Arbiter</em>
    </div>
    <ul class="contact-list">
      <li><svg viewBox="0 0 24 24"><path d="M6.6 10.8a15 15 0 0 0 6.6 6.6l2.2-2.2c.3-.3.7-.4 1-.2 1.1.4 2.3.6 3.6.6.6 0 1 .4 1 1V20c0 .6-.4 1-1 1A17 17 0 0 1 3 4c0-.6.4-1 1-1h3.5c.6 0 1 .4 1 1 0 1.3.2 2.5.6 3.6.1.3 0 .7-.2 1z"/></svg><span class="strong">855-417-6093</span></li>
      <li><svg viewBox="0 0 24 24"><path d="M2 5h20v14H2zM4 7v.5l8 5 8-5V7z"/></svg><span>Milo@frandivo.example</span></li>
      <li><svg viewBox="0 0 24 24"><path d="M12 2a10 10 0 1 0 0 20 10 10 0 0 0 0-20zm0 3a7 7 0 1 1 0 14 7 7 0 0 1 0-14z"/></svg><span>www.frandivo.example</span></li>
      <li><svg viewBox="0 0 24 24"><path d="M12 3 2 12h3v8h5v-5h4v5h5v-8h3z"/></svg><span>3157 N. Wexford Avenue, #51806<br>Denver, CO 80219</span></li>
    </ul>
    <div class="box-truck" role="img" aria-label="Illustration of a white box truck carrying the company name">
      <span class="brand">Frandivo Freight</span>
    </div>
  </section>

  <section class="panel panel--cover">
    <div class="cover-photo" role="img" aria-label="Photo of a blue semi truck speeding down a highway under a pale sky"></div>
    <div class="cover-brand">Frandivo Freight</div>
    <div class="cover-band">
      <span class="fast">FAST</span>
      <span class="relief">SHIPPING RELIEF</span>
    </div>
    <div class="cover-corner"></div>
    <footer class="cover-foot">
      <span class="phone"><svg viewBox="0 0 24 24"><path d="M6.6 10.8a15 15 0 0 0 6.6 6.6l2.2-2.2c.3-.3.7-.4 1-.2 1.1.4 2.3.6 3.6.6.6 0 1 .4 1 1V20c0 .6-.4 1-1 1A17 17 0 0 1 3 4c0-.6.4-1 1-1h3.5c.6 0 1 .4 1 1 0 1.3.2 2.5.6 3.6.1.3 0 .7-.2 1z"/></svg>855-417-6093</span>
      <span class="web">WWW.FRANDIVO.EXAMPLE</span>
    </footer>
  </section>

</main>
</body>
</html>
```